Brightwater Medical business cards

Double sided business cards.

Medical technology consulting company.

Business cards with two names on the front, upper to middle left:

Dr Colin R. Haskell MBBS MAICD +61491578204
Dr Paul Brennagh PhD MIntlTrdLaw +61472019847

Email and website addresses bottom right:

colin@brightwatermedical.com.au
www.brightwatermedical.com.au

Tree logo (as per attached file) on front in a suitable position.

Tag line (as per attached files) on the back.

Need a file format to upload to Desk Ford or Cardmoor.

```html
<!DOCTYPE html>
<html lang="en">
<head>
<meta charset="utf-8">
<title>Brightwater Medical – Business Cards</title>
<link rel="stylesheet" href="https://fonts.googleapis.com/css2?family=Open+Sans:wght@400&family=Roboto+Condensed:wght@700&display=swap">
<style>
  :root {
    --backdrop: #dcdcdc;
    --card: #ffffff;
    --leaf-green: #4a8f3c;
    --bark: #5c1414;
    --card-shadow: rgba(0, 0, 0, 0.18);
  }
  * { margin: 0; padding: 0; box-sizing: border-box; }
  html, body {
    width: 1200px;
    height: 711px;
    overflow: hidden;
    background: radial-gradient(ellipse at 50% 55%, #ececec 0%, var(--backdrop) 70%);
    font-family: "Open Sans", sans-serif;
  }
  .sheet { position: relative; width: 1200px; height: 711px; }
  .card {
    position: absolute;
    top: 195px;
    width: 540px;
    height: 320px;
    background: var(--card);
    border-radius: 22px;
    box-shadow: 0 10px 28px var(--card-shadow);
    overflow: hidden;
  }
  .card--back { left: 40px; }
  .card--front { left: 620px; }

  .brand {
    display: flex;
    align-items: center;
    gap: 12px;
    color: var(--leaf-green);
    font-family: "Open Sans", sans-serif;
    font-weight: 400;
    letter-spacing: 0.02em;
    text-transform: uppercase;
    white-space: nowrap;
  }
  .brand__dot { border-radius: 50%; background: var(--leaf-green); flex: none; }
  .card--back .brand {
    position: absolute;
    left: 0; right: 0; top: 118px;
    justify-content: center;
    font-size: 34px;
  }
  .card--back .brand__dot { width: 22px; height: 22px; }
  .tagline {
    position: absolute;
    left: 0; right: 0; top: 180px;
    text-align: center;
    color: var(--leaf-green);
    font-size: 20px;
    letter-spacing: 0.03em;
    white-space: nowrap;
  }

  .card--front .brand {
    position: absolute;
    right: 34px; top: 34px;
    font-size: 20px;
    gap: 8px;
  }
  .card--front .brand__dot { width: 14px; height: 14px; }

  .people { position: absolute; left: 36px; top: 94px; }
  .person { margin-bottom: 14px; }
  .person__name,
  .person__credentials {
    font-family: "Roboto Condensed", sans-serif;
    font-weight: 700;
    color: var(--leaf-green);
    font-size: 23px;
    line-height: 1.1;
    white-space: nowrap;
  }
  .person__phone {
    display: flex;
    align-items: center;
    gap: 8px;
    margin-top: 3px;
    color: var(--bark);
    font-size: 16px;
  }
  .icon { width: 14px; height: 14px; flex: none; }

  .links {
    position: absolute;
    right: 30px; bottom: 34px;
    text-align: right;
    color: var(--bark);
    font-size: 14px;
    line-height: 1.7;
  }
  .links__row {
    display: flex;
    align-items: center;
    justify-content: flex-end;
    gap: 8px;
    white-space: nowrap;
  }
</style>
</head>
<body>
<main class="sheet">

  <section class="card card--back" aria-label="Business card, back">
    <div class="brand">
      <span class="brand__dot"></span>
      <span class="brand__name">Brightwater Medical</span>
    </div>
    <p class="tagline">Idea | Development | Market Launch</p>
  </section>

  <section class="card card--front" aria-label="Business card, front">
    <div class="brand">
      <span class="brand__dot"></span>
      <span class="brand__name">Brightwater Medical</span>
    </div>

    <div class="people">
      <div class="person">
        <p class="person__name">Dr Colin R. Haskell</p>
        <p class="person__credentials">MBBS MAICD</p>
        <p class="person__phone">
          <svg class="icon" viewBox="0 0 24 24" aria-hidden="true"><path fill="var(--bark)" d="M6.6 10.8a15 15 0 0 0 6.6 6.6l2.2-2.2a1 1 0 0 1 1-.25 11.4 11.4 0 0 0 3.6.57 1 1 0 0 1 1 1V20a1 1 0 0 1-1 1A17 17 0 0 1 3 4a1 1 0 0 1 1-1h3.5a1 1 0 0 1 1 1c0 1.250.2 2.450.57 3.57a1 1 0 0 1-.25 1z"/></svg>
          +61491578204
        </p>
      </div>
      <div class="person">
        <p class="person__name">Dr Paul Brennagh</p>
        <p class="person__credentials">PhD MIntlTrdLaw</p>
        <p class="person__phone">
          <svg class="icon" viewBox="0 0 24 24" aria-hidden="true"><path fill="var(--bark)" d="M6.6 10.8a15 15 0 0 0 6.6 6.6l2.2-2.2a1 1 0 0 1 1-.25 11.4 11.4 0 0 0 3.6.57 1 1 0 0 1 1 1V20a1 1 0 0 1-1 1A17 17 0 0 1 3 4a1 1 0 0 1 1-1h3.5a1 1 0 0 1 1 1c0 1.250.2 2.450.57 3.57a1 1 0 0 1-.25 1z"/></svg>
          +61472019847
        </p>
      </div>
    </div>

    <div class="links">
      <p class="links__row">
        colin@brightwatermedical.com.au
        <svg class="icon" viewBox="0 0 24 24" aria-hidden="true"><rect x="2" y="5" width="20" height="14" rx="2" fill="var(--leaf-green)"/><path d="M3 6l9 7 9-7" fill="none" stroke="#fff" stroke-width="1.8"/></svg>
      </p>
      <p class="links__row">
        www.brightwatermedical.com.au
        <svg class="icon" viewBox="0 0 24 24" aria-hidden="true"><circle cx="12" cy="12" r="10" fill="var(--leaf-green)"/><path d="M2 12h20M12 2c3 3 3 17 0 20M12 2c-3 3-3 17 0 20" fill="none" stroke="#fff" stroke-width="1.4"/></svg>
      </p>
    </div>
  </section>

</main>
</body>
</html>
```